Counsel Atelier

we need all the matirials for the office to speak with the internet site
www.cunatel.example

look stilish and modern yet very respecteble

our logo needs to be our logo and some times

just the letters " Cunatel " done nicely.

We need to send e mails with a design

Firm paper

and our gmail products to look nice when we use google docs

so we need a place for

lawers names and

the cunatel

and logo

and address

and some one to help us do it all

Target Market(s)

Big firms

Industry/Entity Type

Law Firm

Font styles to use
Serif

Requirements
Must have
• Rememrable
• Different yet respectable
• For multi languages
• LAW
• B
• LAWYERS
• BOUTIQUE
Nice to have
• Clean Design
• impressive
• i put on a new card i liked
• We should not put any decorations and beautiful logo
• it's against the law for lawyers
• I have a card that proves that we are smart and boutiques
• This card that I attached as an example
• Makes you little work, and certainly - apart from everyone
• Would love this design idea
• The numbers stated hiding it from top to bottom
• I put my real information integration profile
• The thing is that people should enlighten other options and other card
• This should be accessible designer fee changes
• Still very respectable and serious
• it needs to say among other creative stuff
• Counsel atelier CUNATEL
• TOMAS VELLINGRO
• 052-7164291
• 1@cunatel.example
• www.cunatel.example
• but any smart idea
Should not have
• We have a problam
• It turns out that the law of the Bar Association in
• Our country
• Do not allow to put the firm logo on business cards
• Or office paper
• the logo can only be letters and names
• So we should convey the idea of all sorts of areas along
• As we tried with our logo
• Through the letters themselves
• And their integration with each other

```html
<!DOCTYPE html>
<html lang="en">
<head>
<meta charset="utf-8">
<title>Cunatel – Business Card</title>
<link rel="stylesheet" href="https://fonts.googleapis.com/css2?family=Questrial&family=Arimo:wght@400&display=swap">
<style>
  :root {
    --backdrop: #3a312c;
    --card: #111214;
    --card-edge: #1b1c1f;
    --silver: #b9bbbf;
    --url-grey: #8c8e93;
    --brand-blue: #1d4f9e;
    --text-white: #e9eaec;
    --divider: #8a8c90;
  }
  * { margin: 0; padding: 0; box-sizing: border-box; }
  html, body {
    width: 1200px; height: 864px; overflow: hidden;
    background: var(--backdrop);
  }
  .canvas {
    position: relative; width: 1200px; height: 864px;
  }
  .card {
    position: absolute;
    width: 540px; height: 309px;
    background: var(--card);
    border: 1px solid var(--card-edge);
    border-radius: 4px;
    box-shadow: 0 14px 30px rgba(0,0,0,0.45);
  }
  /* Front */
  .card-front { left: 50px; top: 150px; }
  .front-wordmark {
    position: absolute; left: 0; right: 0; top: 92px;
    text-align: center;
    font-family: "Questrial", sans-serif;
    font-size: 74px; letter-spacing: 3px;
    color: var(--silver);
  }
  .front-url {
    position: absolute; left: 0; right: 0; top: 200px;
    text-align: center;
    font-family: "Arimo", sans-serif;
    font-size: 14px; letter-spacing: 7px;
    color: var(--url-grey);
  }
  /* Back */
  .card-back { left: 610px; top: 405px; }
  .back-wordmark {
    position: absolute; left: 36px; top: 118px;
    font-family: "Questrial", sans-serif;
    font-size: 54px; letter-spacing: 2px;
    color: var(--brand-blue);
  }
  .back-divider {
    position: absolute; left: 282px; top: 70px;
    width: 1px; height: 170px;
    background: linear-gradient(to bottom, transparent, var(--divider) 25%, var(--divider) 75%, transparent);
  }
  .details {
    position: absolute; left: 302px; top: 72px;
    font-family: "Arimo", sans-serif;
    color: var(--text-white);
  }
  .person-name { font-size: 18px; color: var(--brand-blue); letter-spacing: 0.5px; }
  .person-role { font-size: 15px; margin-top: 2px; }
  .address { font-size: 13px; line-height: 18px; margin-top: 12px; }
  .contact-list { list-style: none; margin-top: 12px; }
  .contact-list li {
    display: flex; align-items: center; gap: 9px;
    font-size: 13px; line-height: 21px;
  }
  .contact-icon { width: 12px; height: 12px; fill: var(--brand-blue); flex: none; }
</style>
</head>
<body>
<div class="canvas">
  <section class="card card-front" aria-label="Card front">
    <div class="front-wordmark">Cunatel</div>
    <div class="front-url">www.cunatel.example</div>
  </section>

  <section class="card card-back" aria-label="Card back">
    <div class="back-wordmark">Cunatel</div>
    <div class="back-divider"></div>
    <div class="details">
      <div class="person-name">Tomas Vellingro</div>
      <div class="person-role">Attorney</div>
      <div class="address">2710 Harrowgate Lane<br>Elm Ridge, NY 10987</div>
      <ul class="contact-list">
        <li>
          <svg class="contact-icon" viewBox="0 0 12 12" aria-hidden="true"><path d="M2.5 1h2l1 2.6-1.3 1a6.5 6.5 0 0 0 3.2 3.2l1-1.3L11 7.5v2a1.5 1.5 0 0 1-1.5 1.5A8.5 8.5 0 0 1 1 2.5 1.5 1.5 0 0 1 2.5 1z"/></svg>
          481 2093 7716
        </li>
        <li>
          <svg class="contact-icon" viewBox="0 0 12 12" aria-hidden="true"><path d="M1 2.5h10v7H1z M1.4 3 6 6.6 10.6 3" stroke="#111214" stroke-width="0.9"/></svg>
          mira@cunatel.example
        </li>
        <li>
          <svg class="contact-icon" viewBox="0 0 12 12" aria-hidden="true"><circle cx="6" cy="6" r="5.2"/><path d="M0.8 6h10.4M6 0.8c-2.4 2.8-2.4 7.6 0 10.4M6 0.8c2.4 2.8 2.4 7.6 0 10.4" stroke="#111214" stroke-width="0.8" fill="none"/></svg>
          www.cunatel.example
        </li>
      </ul>
    </div>
  </section>
</div>
</body>
</html>
```